Korvel Bloom , Australian natural body care needs a new product label.

I have just had a logo designed by artflockr and now want this logo added to a product label design. The product is a cleansing, moisturising hand scrub with only natural ingredients and anti microbial essential oils. I have made this product for over 15 years and it needs a new more appropriate image. It was previously called velvet tonic and came in a tube. the new packaging is a white pump pack container. Dimensions for the label are 185mm wide and 80mm high, I have attached a sheet with all of the information required on the label.
Updates

Target Market(s)

anyone with dry skin

Industry/Entity Type

Cosmetics

Requirements
Must have
• professional and upmarket appearance. Be creative and surprise me your take on how this label should look.
Nice to have
• Natural colours, the attached logo should be changed in colour to match the label.

```html
<!DOCTYPE html>
<html lang="en">
<head>
<meta charset="utf-8">
<title>Korvel Bloom Hand Scrub Label</title>
<link rel="stylesheet" href="https://fonts.googleapis.com/css2?family=Raleway:wght@300;400;500;700&display=swap">
<style>
  :root {
    --backdrop: #dcdcdc;
    --label-white: #f4f4f4;
    --leaf-green: #14a820;
    --leaf-green-light: #86dd8c;
    --sea-blue: #1282c6;
    --sea-blue-light: #78c8ec;
    --brand-blue: #3a9ad6;
    --brand-green: #5e9d2a;
    --ink-white: #ffffff;
  }
  * { margin: 0; padding: 0; box-sizing: border-box; }
  html, body {
    width: 1200px; height: 1200px; overflow: hidden;
    background: var(--backdrop);
    font-family: "Raleway", sans-serif;
  }
  .canvas {
    width: 1200px; height: 1200px;
    display: flex; align-items: center; justify-content: center;
  }
  .label {
    width: 540px; height: 1053px;
    display: block;
    box-shadow: 0 4px 18px rgba(0,0,0,0.12);
  }
  .brand-name { font-family: "Raleway", sans-serif; font-weight: 500; fill: var(--brand-blue); }
  .brand-tagline { font-family: "Raleway", sans-serif; font-weight: 500; fill: var(--brand-green); }
  .product-title { font-family: "Raleway", sans-serif; font-weight: 700; fill: var(--ink-white); letter-spacing: 1px; }
  .product-claim { font-family: "Raleway", sans-serif; font-weight: 400; fill: var(--ink-white); }
  .band-note { font-family: "Raleway", sans-serif; font-weight: 400; fill: var(--ink-white); }
</style>
</head>
<body>
<main class="canvas">
  <svg class="label" viewBox="0 0 505 985" xmlns="http://www.w3.org/2000/svg" aria-label="Korvel Bloom hand scrub product label">
    <defs>
      <linearGradient id="label-white-fill" x1="0" x2="1" y1="0" y2="0">
        <stop offset="0" stop-color="#e8e8e8"/>
        <stop offset="0.45" stop-color="#fbfbfb"/>
        <stop offset="1" stop-color="#e6e6e6"/>
      </linearGradient>
      <linearGradient id="green-band-fill" x1="0" x2="1" y1="0" y2="0">
        <stop offset="0" stop-color="var(--leaf-green)"/>
        <stop offset="0.42" stop-color="var(--leaf-green-light)"/>
        <stop offset="1" stop-color="var(--leaf-green)"/>
      </linearGradient>
      <linearGradient id="blue-band-fill" x1="0" x2="1" y1="0" y2="0">
        <stop offset="0" stop-color="var(--sea-blue)"/>
        <stop offset="0.4" stop-color="var(--sea-blue-light)"/>
        <stop offset="1" stop-color="var(--sea-blue)"/>
      </linearGradient>
      <linearGradient id="texture-fill" x1="0" x2="1" y1="0" y2="1">
        <stop offset="0" stop-color="#ffffff" stop-opacity="0.05"/>
        <stop offset="1" stop-color="#ffffff" stop-opacity="0.35"/>
      </linearGradient>
    </defs>

    <rect class="label-base" x="0" y="0" width="505" height="985" fill="url(#label-white-fill)"/>

    <g class="brand-block">
      <circle cx="252" cy="150" r="16" fill="var(--brand-blue)"/>
      <text class="brand-name" x="252" y="255" text-anchor="middle" font-size="46">Korvel Bloom</text>
      <text class="brand-tagline" x="252" y="281" text-anchor="middle" font-size="13">naturally beautiful skincare</text>
    </g>

    <path class="green-band" d="M0,378 C160,335 340,320 505,278 L505,985 L0,985 Z" fill="url(#green-band-fill)"/>

    <path class="texture-area" role="img" aria-label="White halftone dot texture sweeping across the green band"
          d="M0,870 C120,800 260,700 505,600 L505,790 C300,790 150,870 0,895 Z" fill="url(#texture-fill)"/>

    <path class="blue-band" d="M0,895 C150,872 300,790 505,790 L505,980 L0,980 Z" fill="url(#blue-band-fill)"/>
    <rect class="band-edge" x="0" y="980" width="505" height="5" fill="var(--leaf-green-light)"/>

    <g class="product-copy">
      <text class="product-title" x="252" y="455" text-anchor="middle" font-size="66">HAND SCRUB</text>
      <text class="product-claim" x="252" y="535" text-anchor="middle" font-size="33">Dry &amp; damaged hand repair</text>
      <text class="product-claim" x="252" y="580" text-anchor="middle" font-size="33">results</text>
    </g>

    <g class="band-copy">
      <text class="band-note" x="14" y="927" font-size="26">Net wt. 250g</text>
      <text class="band-note" x="492" y="878" text-anchor="end" font-size="33">moisturising with</text>
      <text class="band-note" x="492" y="924" text-anchor="end" font-size="33">essential oils</text>
    </g>
  </svg>
</main>
</body>
</html>
```